Harborne Cellarbook: the premier wine registry - (need business cards)

We have a logo designed, and now we need business cards for our 3 founders. Harborne Cellarbook is the premier wine registry for weddings. I am envisioning the wine glass with the heart in it as our signature symbol. (FYI- on the red background file, only use the part that has the red background; the brown colors are not relevant)

```html
<!DOCTYPE html>
<html lang="en">
<head>
<meta charset="utf-8">
<title>Harborne Cellarbook — Business Cards</title>
<link rel="stylesheet" href="https://fonts.googleapis.com/css2?family=Montserrat:wght@400;500&display=swap">
<style>
  :root {
    --backdrop: #1c1c1c;
    --card: #9b2452;
    --ink: #f4f1f2;
    --ink-soft: #e2d3da;
    --rule: rgba(244, 241, 242, 0.55);
  }
  * { box-sizing: border-box; margin: 0; padding: 0; }
  html, body {
    width: 1200px;
    height: 1200px;
    overflow: hidden;
    background: var(--backdrop);
    font-family: "Montserrat", sans-serif;
    color: var(--ink);
  }
  .sheet {
    width: 1200px;
    height: 1200px;
    display: flex;
    flex-direction: column;
    align-items: center;
    justify-content: center;
    gap: 44px;
  }
  .card {
    position: relative;
    width: 900px;
    height: 514px;
    background: var(--card);
    border-radius: 34px;
    overflow: hidden;
  }
  .wordmark {
    font-weight: 500;
    text-transform: uppercase;
    letter-spacing: 0.3em;
    white-space: nowrap;
    color: var(--ink);
  }
  .card--front .wordmark {
    position: absolute;
    left: 0; right: 0;
    top: 50%;
    transform: translateY(-50%);
    text-align: center;
    font-size: 34px;
  }
  .card--back .wordmark {
    position: absolute;
    left: 0; right: 0;
    top: 96px;
    text-align: center;
    font-size: 36px;
  }
  .identity {
    position: absolute;
    right: 490px;
    top: 272px;
    text-align: right;
    text-transform: uppercase;
  }
  .identity__name {
    font-size: 25px;
    font-weight: 500;
    letter-spacing: 0.04em;
  }
  .identity__role {
    margin-top: 6px;
    font-size: 18px;
    font-weight: 400;
    letter-spacing: 0.08em;
    color: var(--ink-soft);
  }
  .divider {
    position: absolute;
    left: 436px;
    top: 262px;
    width: 1px;
    height: 160px;
    background: var(--rule);
  }
  .contact {
    position: absolute;
    left: 462px;
    top: 262px;
    font-size: 19px;
    line-height: 1.5;
    letter-spacing: 0.02em;
  }
  .contact__list { list-style: none; }
  .contact__item {
    display: flex;
    align-items: center;
    gap: 12px;
  }
  .contact__icon {
    width: 20px;
    height: 20px;
    flex: none;
    fill: none;
    stroke: var(--ink);
    stroke-width: 1.8;
  }
  .contact__address {
    margin-top: 10px;
    font-style: normal;
    font-size: 20px;
    line-height: 1.35;
  }
</style>
</head>
<body>
<main class="sheet">
  <section class="card card--front" aria-label="Card front">
    <p class="wordmark">Harborne Cellarbook</p>
  </section>

  <section class="card card--back" aria-label="Card back">
    <p class="wordmark">Harborne Cellarbook</p>

    <div class="identity">
      <p class="identity__name">Everett Lindqvist</p>
      <p class="identity__role">Managing Director</p>
    </div>

    <div class="divider"></div>

    <div class="contact">
      <ul class="contact__list">
        <li class="contact__item">
          <svg class="contact__icon" viewBox="0 0 20 20" aria-hidden="true"><path d="M3 7c0-2 3-3 7-3s7 1 7 3l-3 1-1-2H7L6 8z"/><rect x="5" y="9" width="10" height="7" rx="1"/></svg>
          <span>616 555 0148</span>
        </li>
        <li class="contact__item">
          <svg class="contact__icon" viewBox="0 0 20 20" aria-hidden="true"><rect x="2" y="5" width="16" height="11" rx="1"/><path d="M2 6l8 6 8-6"/></svg>
          <span>info@harbornecellarbook.com</span>
        </li>
        <li class="contact__item">
          <svg class="contact__icon" viewBox="0 0 20 20" aria-hidden="true"><circle cx="10" cy="10" r="8"/><ellipse cx="10" cy="10" rx="3.5" ry="8"/><path d="M2 10h16M4 5.5h12M4 14.5h12"/></svg>
          <span>www.harbornecellarbook.com</span>
        </li>
      </ul>
      <address class="contact__address">
        118 Larkspur Street NE<br>
        Suite 210, Elm Harbor<br>
        MI 49012
      </address>
    </div>
  </section>
</main>
</body>
</html>
```